Optometrist/Eye Care Clinic Business card with new logo attached

We are a small, independent eye care clinic in Canada. We have recently updated our logo (as attached), and would like a professional, modern and health care oriented business card to highlight our office details and our optometrist. We'd like to incorporate the blue colours as seen on our logo.

Target Market(s)

demographic: age 35-65 male/female equal

Industry/Entity Type

Health Care

Contact Information for Business Card

Name of clinic: "Amber Hollow Eye Care Optometry"

Font styles to use
Sans Serif

Colors
0355a3

Requirements
Must have
• our website: amberholloweyecare.net
• Dr Selma Okonkwo
• Optometrist
• 312-617 E Larkspur Ave
• Vancouver BC V7R 3P8
• P: 604-555-0193
• E: info@amberholloweyecare.net
Nice to have
• front side: logo/name of clinic as seen on logo attached and website
• backside: logo on the left side, and name/title/address/phone/email

```html
<!DOCTYPE html>
<html lang="en">
<head>
<meta charset="utf-8">
<title>Amber Hollow Eye Care Optometry – Business Card</title>
<link rel="stylesheet" href="https://fonts.googleapis.com/css2?family=Lato:wght@400;700&family=Open+Sans:wght@400;700&display=swap">
<style>
  :root {
    --brand-blue: #0355a3;
    --deep-navy: #0b3d6b;
    --logo-teal: #17527a;
    --logo-dark: #0e3c63;
    --paper: #ffffff;
    --backdrop: #c6c6c6;
    --text-light: #ffffff;
  }
  * { box-sizing: border-box; margin: 0; padding: 0; }
  html, body {
    width: 1200px;
    height: 1138px;
    overflow: hidden;
    background: var(--backdrop);
  }
  .canvas {
    position: relative;
    width: 1200px;
    height: 1138px;
  }
  .card {
    position: absolute;
    overflow: hidden;
  }

  /* ---------- Front card ---------- */
  .card-front {
    left: 249px;
    top: 166px;
    width: 730px;
    height: 413px;
    background: var(--paper);
  }
  .front-brand {
    position: absolute;
    left: 0;
    top: 0;
    width: 364px;
    height: 100%;
    text-align: center;
  }
  .brand-dot {
    position: absolute;
    left: 132px;
    top: 95px;
    width: 100px;
    height: 100px;
    border-radius: 50%;
    background: var(--logo-teal);
  }
  .brand-name {
    position: absolute;
    left: 0;
    width: 100%;
    font-family: "Lato", sans-serif;
    font-weight: 400;
    font-size: 24px;
    line-height: 34px;
    letter-spacing: 4px;
    color: var(--logo-teal);
    text-transform: uppercase;
  }
  .card-front .brand-name { top: 232px; }

  .divider {
    position: absolute;
    left: 364px;
    top: 0;
    width: 10px;
    height: 100%;
  }
  .details-panel {
    position: absolute;
    left: 372px;
    top: 0;
    right: 0;
    height: 100%;
    background: var(--brand-blue);
    color: var(--text-light);
    font-family: "Open Sans", sans-serif;
  }
  .doctor-name {
    position: absolute;
    left: 23px;
    top: 88px;
    font-family: "Lato", sans-serif;
    font-weight: 700;
    font-size: 24px;
    letter-spacing: 0.3px;
    text-transform: uppercase;
  }
  .doctor-title {
    position: absolute;
    left: 23px;
    top: 118px;
    font-family: "Lato", sans-serif;
    font-weight: 400;
    font-size: 21px;
    text-transform: uppercase;
  }
  .contact-line {
    position: absolute;
    left: 23px;
    display: flex;
    align-items: center;
    gap: 6px;
    font-size: 18px;
    line-height: 24px;
    white-space: nowrap;
  }
  .contact-line svg { width: 16px; height: 16px; flex: none; }
  .contact-phone { top: 171px; }
  .contact-email { top: 201px; }
  .contact-address { top: 258px; align-items: flex-start; letter-spacing: 0.4px; }
  .contact-address svg { margin-top: 4px; }

  /* ---------- Back card ---------- */
  .card-back {
    left: 256px;
    top: 602px;
    width: 715px;
    height: 418px;
    background: var(--brand-blue);
    text-align: center;
  }
  .card-back .brand-dot {
    left: 307px;
    top: 58px;
    background: var(--logo-dark);
  }
  .card-back .brand-name {
    top: 218px;
    color: var(--logo-dark);
    font-size: 28px;
    line-height: 38px;
    letter-spacing: 6px;
  }
  .website {
    position: absolute;
    left: 0;
    width: 100%;
    top: 350px;
    font-family: "Open Sans", sans-serif;
    font-size: 19px;
    letter-spacing: 1.5px;
    color: var(--text-light);
  }
</style>
</head>
<body>
<main class="canvas">

  <section class="card card-front" aria-label="Business card, details side">
    <div class="front-brand">
      <span class="brand-dot" aria-hidden="true"></span>
      <p class="brand-name">Amber Hollow<br>Eye Care<br>Optometry</p>
    </div>

    <svg class="divider" viewBox="0 0 10 413" aria-hidden="true">
      <rect x="0" y="0" width="5" height="413" fill="var(--deep-navy)"/>
    </svg>

    <div class="details-panel">
      <svg style="position:absolute;left:-8px;top:94px" width="26" height="40" viewBox="0 0 26 40" aria-hidden="true">
        <polyline points="4,2 20,20 4,38" fill="none" stroke="var(--text-light)" stroke-width="3"/>
      </svg>
      <h1 class="doctor-name">Dr Selma Okonkwo</h1>
      <p class="doctor-title">Optometrist</p>

      <p class="contact-line contact-phone">
        <svg viewBox="0 0 16 16" aria-hidden="true"><circle cx="8" cy="8" r="7" fill="none" stroke="#fff" stroke-width="1.3"/><path d="M6 4.5 L7.3 6.6 L6.6 7.4 Q7.6 9.4 9 10 L9.8 9.2 L11.6 10.6 L10.6 11.8 Q6.5 11 4.8 6 Z" fill="#fff"/></svg>
        604-555-0193
      </p>
      <p class="contact-line contact-email">
        <svg viewBox="0 0 16 16" aria-hidden="true"><rect x="1" y="5" width="14" height="9" rx="1" fill="#fff"/><polyline points="1.5,5.5 8,10 14.5,5.5" fill="none" stroke="var(--brand-blue)" stroke-width="1.2"/><path d="M3 5 L8 1.5 L13 5" fill="none" stroke="#fff" stroke-width="1.2"/></svg>
        info@amberholloweyecare.net
      </p>
      <p class="contact-line contact-address">
        <svg viewBox="0 0 16 16" aria-hidden="true"><circle cx="8" cy="8" r="7" fill="none" stroke="#fff" stroke-width="1.3"/><path d="M8 12.5 Q4.8 8.6 4.8 6.6 A3.2 3.2 0 0 1 11.2 6.6 Q11.2 8.6 8 12.5 Z" fill="#fff"/><circle cx="8" cy="6.6" r="1.2" fill="var(--brand-blue)"/></svg>
        <span>312-617 E Larkspur Ave<br>Vancouver BC V7R 3P8</span>
      </p>
    </div>
  </section>

  <section class="card card-back" aria-label="Business card, brand side">
    <span class="brand-dot" aria-hidden="true"></span>
    <p class="brand-name">Amber Hollow<br>Eye Care<br>Optometry</p>
    <p class="website">www.amberholloweyecare.net</p>
  </section>

</main>
</body>
</html>
```